Magnetic car sign for Pillarwise Structural Advisors

I already have a logo, however I now need a design for a magnetic car sign. My company is Pillarwise Structural Advisors, and I am located in Perth, Western Australia. I operate in the building and construction industry. I work largely with architects, building designers, builders, and engineers.

Target Market(s)

Everyone

Industry/Entity Type

It Company

Requirements
Nice to have
• My car is gun metal grey (dark grey). I want to sign to be based on a dark background so that it blends in with the car.

```html
<!DOCTYPE html>
<html lang="en">
<head>
<meta charset="utf-8">
<title>Pillarwise Structural Advisors – Magnetic Car Sign</title>
<link rel="stylesheet" href="https://fonts.googleapis.com/css2?family=Cinzel:wght@600;700&family=Open+Sans:wght@400&display=swap">
<style>
  :root {
    --backdrop: #e9e9ea;
    --sign-dark: #2f2f31;
    --brand-red: #7a2f26;
    --text-light: #ffffff;
    --rule-grey: #bdbdbd;
  }
  html, body {
    margin: 0;
    padding: 0;
    width: 1200px;
    height: 1050px;
    overflow: hidden;
    background: var(--backdrop);
  }
  .car-sign {
    display: block;
    width: 1200px;
    height: 1050px;
  }
  .sign-panel, .sign-crest { fill: var(--sign-dark); }
  .web-band { fill: var(--brand-red); }
  .company-name {
    font-family: "Cinzel", "Times New Roman", serif;
    font-weight: 700;
    fill: var(--text-light);
  }
  .company-descriptor {
    font-family: "Cinzel", "Times New Roman", serif;
    font-weight: 600;
    fill: var(--text-light);
  }
  .descriptor-rule { stroke: var(--rule-grey); stroke-width: 2; }
  .contact-text {
    font-family: "Open Sans", Arial, sans-serif;
    font-weight: 400;
    fill: var(--text-light);
  }
</style>
</head>
<body>
<svg class="car-sign" viewBox="0 0 1200 1050" xmlns="http://www.w3.org/2000/svg">
  <title>Pillarwise Structural Advisors magnetic car sign</title>

  <circle class="sign-crest" cx="600" cy="338" r="185"/>
  <rect class="sign-panel" x="50" y="362" width="1100" height="535" rx="18"/>

  <text class="company-name" x="600" y="622" text-anchor="middle" font-size="112" textLength="1010" lengthAdjust="spacingAndGlyphs">PILLARWISE</text>

  <line class="descriptor-rule" x1="94" y1="664" x2="250" y2="664"/>
  <text class="company-descriptor" x="600" y="677" text-anchor="middle" font-size="40" textLength="680" lengthAdjust="spacingAndGlyphs">STRUCTURAL ADVISORS</text>
  <line class="descriptor-rule" x1="950" y1="664" x2="1106" y2="664"/>

  <rect class="web-band" x="50" y="705" width="1100" height="76"/>
  <text class="contact-text" x="600" y="764" text-anchor="middle" font-size="62">www.pillarwisesa.com</text>

  <text class="contact-text" x="600" y="866" text-anchor="middle" font-size="72">0400 555 218</text>
</svg>
</body>
</html>
```